Leave Behind Flyer Project for Print

Project Goal: Create a leave-behind flyer promoting Skyrun Motion to our customers: Multihousing property managers, hospitality, boutique gyms, high schools, colleges & resellers.

Theme: entry-level commercial products for a value price

Theme Heading: COMMERCIAL – GRADE GYM EQUIPMENT THAT WON’T BREAK THE BANK

Description: Skyrun Motion Cardio Equipment is a boutique brand of incredibly affordable, commercial fitness equipment. Save thousands by letting Skyrun Motion be your turnkey solution for cardio fitness equipment. Search now for a low-price guarantee, quality fitness equipment with excellent customer service.

Company Promoting it: Coral Vigor Partners

Company Address: 4817 Heron Way, Fort Myers, FL 33358 | Phone : (239) 555-0174

Email: Sales@CoralVigorPartners.example website: CoralVigorPartners.example
Company Logo:

Products Being Promoted: Skyrun Motion – links to photos and descriptions below:
K4 Treadmill
https://skyrunmotion.example/product/k4/
P3 Elliptical
https://skyrunmotion.example/product/p3/
T2 Upright Bike
https://skyrunmotion.example/product/t2/
V9 Recumbent Bike
https://skyrunmotion.example/product/v9/

Flyer size: 8.5” x 11,” Vertical, Full Color, Front / Back

InDesign Template: https://files.presslumo.example/templates/presslumo.example/flyer-8.5inx11in-v.indd.zip

Photoshop Template: https://files.presslumo.example/templates/presslumo.example/flyer-8.5inx11in-v.psd.zip

Illustrator: https://files.presslumo.example/templates/presslumo.example/flyer-8.5inx11in-v.ai.zip

Target Market(s)

Multihousing property managers, hospitality, boutique gyms, high schools, colleges & resellers.

Industry/Entity Type

Fitness equipment

Requirements
Must have
• Equipment pictures, equipmet model numbers, description
Nice to have
• Modern Flyer

```html
<!DOCTYPE html>
<html lang="en">
<head>
<meta charset="utf-8">
<title>Skyrun Motion Flyer – Coral Vigor Partners</title>
<link rel="stylesheet" href="https://fonts.googleapis.com/css2?family=Montserrat:wght@500;600;700;800&family=Raleway:wght@400;500&display=swap">
<style>
:root{
  --bg:#f1f1f1;
  --ink:#222;
  --dark:#141110;
  --gold:#e8ad1e;
  --blue:#1f4fa3;
  --blue-deep:#173f88;
  --panel:#efefef;
  --line:#cfcfcf;
  --white:#fff;
}
*{margin:0;padding:0;box-sizing:border-box}
html,body{width:1200px;height:2626px;overflow:hidden;background:var(--bg)}
body{position:relative;font-family:"Raleway",sans-serif;color:var(--ink)}
.page{position:absolute;left:320px;width:560px;height:722px;box-shadow:0 6px 18px rgba(0,0,0,.18);overflow:hidden}
.front{top:1025px;background:var(--dark)}
.back{top:1808px;background:var(--white)}

/* front */
.hero-photo{position:absolute;inset:0 0 60px 0;background:
  radial-gradient(ellipse at 30% 35%,rgba(214,96,32,.55),transparent 55%),
  radial-gradient(ellipse at 75% 30%,rgba(190,80,30,.35),transparent 50%),
  linear-gradient(180deg,#2a2420 0%,#3a2a20 35%,#1b1714 62%,#0f0d0c 100%)}
.brand{position:absolute;display:flex;align-items:center;gap:8px;font-family:"Montserrat",sans-serif;font-weight:600;white-space:nowrap}
.brand-dot{width:26px;height:26px;border-radius:50%;background:var(--gold);flex:none}
.front .brand{top:26px;left:0;right:0;justify-content:center;color:var(--white);font-size:20px}
.kicker{position:absolute;top:397px;width:100%;text-align:center;font-family:"Montserrat",sans-serif;font-weight:600;font-size:18px;color:var(--gold)}
.headline{position:absolute;top:420px;width:100%;text-align:center;font-family:"Montserrat",sans-serif;font-weight:800;font-size:38px;line-height:47px;color:var(--white);letter-spacing:.3px}
.desc-title{position:absolute;top:520px;width:100%;text-align:center;font-family:"Montserrat",sans-serif;font-weight:600;font-size:18px;color:var(--gold)}
.desc{position:absolute;top:548px;left:50px;right:50px;text-align:center;font-size:11.2px;line-height:16.5px;color:#d6d2cf}
.email-pill{position:absolute;top:632px;left:172px;width:240px;height:22px;background:var(--gold);display:flex;align-items:center;justify-content:center;gap:6px;font-family:"Montserrat",sans-serif;font-weight:700;font-size:10.5px;color:#2a2000}
.contact-bar{position:absolute;left:0;right:0;bottom:0;height:60px;background:linear-gradient(180deg,var(--blue),var(--blue-deep));display:flex;align-items:center;justify-content:center;gap:18px;color:var(--white);font-family:"Montserrat",sans-serif;font-weight:500;font-size:11px}
.contact-bar span{display:flex;align-items:center;gap:6px}
.contact-bar svg{flex:none}

/* back */
.promo-band{position:absolute;top:0;right:0;width:350px;height:50px;background:var(--gold);clip-path:polygon(0 0,100% 0,100% 100%,40px 100%);display:flex;align-items:center;justify-content:center;padding-left:40px;font-family:"Montserrat",sans-serif;font-weight:700;font-size:11px;color:#3a2a00;white-space:nowrap}
.back .brand{top:15px;left:24px;gap:6px;color:var(--blue);font-size:12px}
.back .brand-dot{width:17px;height:17px}
.product{position:absolute;left:20px;width:520px}
.product-tab{position:absolute;top:0;left:0;height:13px;width:120px;background:var(--blue);clip-path:polygon(0 0,88% 0,100% 100%,0 100%);color:var(--white);font-family:"Montserrat",sans-serif;font-weight:700;font-size:7.5px;line-height:13px;padding-left:8px;white-space:nowrap}
.product-box{position:absolute;top:13px;left:0;width:520px;height:124px;background:var(--panel);border:1px solid var(--line);border-top:2px solid var(--blue)}
.product-copy{position:absolute;top:10px;font-size:7.4px;line-height:9.7px;color:#333}
.product-copy p+p{margin-top:9px}
.product-img{position:absolute;top:8px;width:105px;height:106px;border-radius:4px;background:radial-gradient(ellipse at 50% 55%,#5a5d63 0%,#2b2d31 45%,rgba(230,230,230,0) 72%)}
.img-right .product-copy{left:20px;width:360px}
.img-right .product-img{right:4px}
.img-left .product-copy{left:105px;width:405px}
.img-left .product-img{left:6px}
.back .contact-bar{height:58px}
</style>
</head>
<body>

<section class="page front" aria-label="Flyer front">
  <div class="hero-photo" role="img" aria-label="Photo of a dark industrial gym with rows of treadmills and tall windows glowing orange"></div>
  <div class="brand"><span class="brand-dot"></span>Coral Vigor Partners</div>
  <p class="kicker">COMMERCIAL – GRADE GYM</p>
  <h1 class="headline">EQUIPMENT THAT WON’T<br>BREAK THE BANK</h1>
  <h2 class="desc-title">Description:</h2>
  <p class="desc">Skyrun Motion Cardio Equipment is a boutique brand of incredibly affordable, commercial fitness equipment. Save thousands by letting Skyrun Motion be your turnkey solution for cardio fitness equipment. Search now for a low-price guarantee, quality fitness equipment with excellent customer service.</p>
  <div class="email-pill">
    <svg width="16" height="11" viewBox="0 0 16 11"><rect x=".75" y=".75" width="14.5" height="9.5" fill="none" stroke="#2a2000" stroke-width="1.3"/><path d="M1 1l7 5 7-5" fill="none" stroke="#2a2000" stroke-width="1.3"/></svg>
    Sales@CoralVigorPartners.example
  </div>
  <footer class="contact-bar">
    <span><svg width="12" height="16" viewBox="0 0 12 16"><path d="M6 1a4.5 4.5 0 0 0-4.5 4.5C1.5 9 6 13 6 13s4.5-4 4.5-7.5A4.5 4.5 0 0 0 6 1z" fill="none" stroke="#e8ad1e" stroke-width="1.6"/><circle cx="6" cy="5.5" r="1.6" fill="#e8ad1e"/><path d="M2 15h8" stroke="#e8ad1e" stroke-width="1.6"/></svg>4817 Heron Way, Fort Myers</span>
    <span><svg width="15" height="15" viewBox="0 0 16 16"><circle cx="8" cy="8" r="6.8" fill="none" stroke="#e8ad1e" stroke-width="1.4"/><ellipse cx="8" cy="8" rx="3" ry="6.8" fill="none" stroke="#e8ad1e" stroke-width="1.2"/><path d="M1.5 8h13" stroke="#e8ad1e" stroke-width="1.2"/></svg>CoralVigorPartners.example</span>
    <span><svg width="15" height="15" viewBox="0 0 16 16"><path d="M3 1.5l3 3-1.6 1.8a9 9 0 0 0 5.3 5.3L11.5 10l3 3-2 2C6 15 1 10 1 3.5z" fill="none" stroke="#e8ad1e" stroke-width="1.4" stroke-linejoin="round"/></svg>(239) 555-0174</span>
  </footer>
</section>

<section class="page back" aria-label="Flyer back">
  <div class="brand"><span class="brand-dot"></span>Coral Vigor Partners</div>
  <div class="promo-band">PRODUCTS BEING PROMOTED: SKYRUN MOTION</div>

  <article class="product img-right" style="top:70px">
    <div class="product-tab">K4 (AC/DC) TREADMILL</div>
    <div class="product-box">
      <div class="product-copy">
        <p>With its powerful motor and durable frame, the K4 Treadmill is the perfect choice for fitness enthusiasts. This treadmill offers a great deal of versatility with its highlighted features – a high-efficiency 4.25 HP DC motor OR 3.5 HP AC motor, a 60”x20” lubricant-infused, thermoplastic polyurethane (TPU) running belt, and a shock-absorbing, maintenance-free deck.</p>
        <p>The K4 also offers additional comfort features, such as contact and telemetric heart-rate sensors, a cooling fan, speakers, and USB charging port. Perfectly designed for maximum performance and portability, the K4’s small footprint and easy-to-move front-mounted dual wheels make it easy to move from spot to spot. With its full commercial components on a durable light-commercial frame and Zinc-dipped anti-corrosion coating for superior rust protection, the K4 Treadmill is a reliable and tough machine that is perfect for any commercial facility!</p>
      </div>
      <div class="product-img" role="img" aria-label="Product photo of the K4 treadmill"></div>
    </div>
  </article>

  <article class="product img-left" style="top:213px">
    <div class="product-tab">P3 Elliptical</div>
    <div class="product-box">
      <div class="product-img" role="img" aria-label="Product photo of the P3 elliptical"></div>
      <div class="product-copy">
        <p>The P3 Elliptical is the perfect solution to your fitness routine. This light commercial elliptical offers an ergonomic design, low step-up height, and a 20” natural stride, all perfect for everyday use. The environmentally friendly machine is a self-powered cordless model and is designed to last; features include a zinc-dipped anti-corrosion coating for superior rust protection,</p>
        <p>along with a durable light-commercial frame and full-commercial components. The intuitive touchpad offers you control over your workout with a quick resistance shifter – no need to get off the machine to adjust. You can keep track of your performance and heart rate with the contact and telemetric heart-rate sensors and read while working out with the convenient reading rack/tablet holder. Whether you’re a beginner or an advanced fitness enthusiast, the P3 Elliptical is perfect for your fitness studio or facility. Experience maximum performance and a natural, unhindered workout with the P3 Elliptical.</p>
      </div>
    </div>
  </article>

  <article class="product img-right" style="top:359px">
    <div class="product-tab">T2 UPRIGHT BIKE</div>
    <div class="product-box">
      <div class="product-copy" style="top:14px">
        <p>The T2 Upright Bike is built with fitness enthusiasts in mind. Our light commercial grade construction offers a powerful blend of convenience and durability. With the unique, self-powered cordless design, large ergonomic pedals with adjustable straps, and an easy-pull adjustable seat – your riding experience will be smooth, secure, and comfortable. Looking for an extra challenge?</p>
        <p>Factor in the triathlon-style handlebars and 13 levels of resistance for a rigorous hill-climbing workout. Enjoy additional convenience with our secure tablet holder and reading rack. Plus, our zinc-dipped anti-corrosion coating and small footprint for easy storage ensure the T2 Upright Bike will be a reliable workout partner for years to come. Get your new ride today!</p>
      </div>
      <div class="product-img" role="img" aria-label="Product photo of the T2 upright bike"></div>
    </div>
  </article>

  <article class="product img-left" style="top:505px">
    <div class="product-tab">V9 RECUMBENT BIKE</div>
    <div class="product-box">
      <div class="product-img" role="img" aria-label="Product photo of the V9 recumbent bike"></div>
      <div class="product-copy" style="top:14px">
        <p>The V9 Recumbent Bike is the perfect combination of convenience and comfort for the fitness enthusiast looking for a premium, light commercial experience! This bike features an ergonomic and adjustable design, convenient oversized pedals, adjustable straps, and a walk-through frame design.</p>
        <p>With an easy-glide, 13-level adjustable seat and contact and telemetric heart-rate sensors, you’ll have access to various settings to maximize your workout. The integrated reading rack and tablet holder allow you to access entertainment while exercising easily, and an anti-corrosion zinc-dipped coating ensures superior rust protection. All these features are contained within a full commercial-grade frame that occupies only a small footprint, making the V9 Recumbent Bike a must-have for any fitness enthusiast looking for the most out of their exercise routine.</p>
      </div>
    </div>
  </article>

  <footer class="contact-bar">
    <span><svg width="12" height="16" viewBox="0 0 12 16"><path d="M6 1a4.5 4.5 0 0 0-4.5 4.5C1.5 9 6 13 6 13s4.5-4 4.5-7.5A4.5 4.5 0 0 0 6 1z" fill="none" stroke="#e8ad1e" stroke-width="1.6"/><circle cx="6" cy="5.5" r="1.6" fill="#e8ad1e"/><path d="M2 15h8" stroke="#e8ad1e" stroke-width="1.6"/></svg>4817 Heron Way, Fort Myers</span>
    <span><svg width="15" height="15" viewBox="0 0 16 16"><path d="M3 1.5l3 3-1.6 1.8a9 9 0 0 0 5.3 5.3L11.5 10l3 3-2 2C6 15 1 10 1 3.5z" fill="none" stroke="#e8ad1e" stroke-width="1.4" stroke-linejoin="round"/></svg>(239) 555-0174</span>
    <span><svg width="15" height="15" viewBox="0 0 16 16"><circle cx="8" cy="8" r="6.8" fill="none" stroke="#e8ad1e" stroke-width="1.4"/><ellipse cx="8" cy="8" rx="3" ry="6.8" fill="none" stroke="#e8ad1e" stroke-width="1.2"/><path d="M1.5 8h13" stroke="#e8ad1e" stroke-width="1.2"/></svg>CoralVigorPartners.example</span>
  </footer>
</section>

</body>
</html>
```